Landing Page - Lending & Lantern

Need a singular landing page that will eventually link to podcast and direct people to my page. I need it to work with FernoTrack.

The page is geared about small business owners and linking them with high quality banker to obtain financing. It should be professional, connect to bourbon as an underlying tone. It's all about qualify and integrity.

It needs to be put in Wordpress.
I don't know the difference between coded and uncoded, I just want it done.

Target Market(s)

Business Owners and those needing help with financing. The people we're trying to help aren't rich, they are successful but need help.

Industry/Entity Type

Finance & Bourbon

Coding

Coded - Design and coding required

Number of Pages Required

1 page

Colors
0054AA
0677BA
7BADD7
CADEEF
E8F1F8
0094D4
00A9DD
6FCCEA
C7EBF8
E9F6FB

Requirements
Must have
• Link to send email
Nice to have
• Use colors and fonts in branding.

```html
<!DOCTYPE html>
<html lang="en">
<head>
<meta charset="utf-8">
<title>Lending &amp; Lantern</title>
<link href="https://fonts.googleapis.com/css2?family=Libre+Caslon+Text:wght@400;700&family=Roboto:wght@400;500;700&display=swap" rel="stylesheet">
<style>
:root{
  --teal:#0fa49b;
  --teal-dark:#0b8a83;
  --brown:#774a28;
  --ink:#1d1d1d;
  --text:#4a4a4a;
  --muted:#7a7a7a;
  --mist:#eef8f7;
  --line:#e6e6e6;
  --footer:#1b1b1b;
  --footer-bar:#111111;
  --white:#ffffff;
  --star:#f2b91c;
}
*{margin:0;padding:0;box-sizing:border-box}
html,body{width:1200px;height:4054px;overflow:hidden}
body{font-family:"Roboto",Arial,sans-serif;color:var(--text);background:var(--white);position:relative}
.serif{font-family:"Libre Caslon Text",Georgia,serif}
a{color:inherit;text-decoration:none}
.abs{position:absolute}
.section-title{position:absolute;left:0;width:1200px;text-align:center;font-family:"Libre Caslon Text",Georgia,serif;font-size:34px;color:var(--ink);letter-spacing:.5px}
.btn{display:inline-flex;align-items:center;gap:8px;border-radius:30px;font-weight:700;font-size:15px;text-transform:uppercase}
.btn svg{width:15px;height:15px}

/* header */
.site-header{position:absolute;top:0;left:0;width:1200px;height:124px;background:var(--white)}
.brand{position:absolute;left:110px;top:30px;display:flex;align-items:center;gap:10px;font-family:"Libre Caslon Text",Georgia,serif;font-weight:700;font-size:26px;color:var(--brown);line-height:1.05;width:160px}
.brand-dot{width:14px;height:14px;border-radius:50%;background:var(--teal);flex:none}
.call{position:absolute;left:699px;top:20px;display:flex;align-items:center;gap:14px}
.call-icon{width:38px;height:38px;border-radius:50%;background:var(--brown);display:flex;align-items:center;justify-content:center}
.call small{display:block;font-size:12px;color:var(--text)}
.call strong{font-size:19px;color:var(--ink);font-weight:500}
.login{position:absolute;left:947px;top:19px;width:141px;height:42px;background:var(--teal);color:var(--white);justify-content:center;font-size:14px}
.nav{position:absolute;top:84px;left:458px;display:flex;font-size:14px;color:var(--ink)}
.nav span.sep{margin:0 24px}

/* hero */
.hero{position:absolute;top:124px;left:0;width:1200px;height:622px;background:linear-gradient(100deg,#3b3833 0%,#6a5f52 30%,#a48d74 55%,#cdb9a2 75%,#8a7a68 100%)}
.hero-title{position:absolute;left:112px;top:150px;font-size:68px;line-height:76px;color:var(--white)}
.hero-copy{position:absolute;left:115px;top:325px;width:440px;font-size:15px;line-height:28px;color:var(--white);font-weight:500}
.hero .btn{position:absolute;left:115px;top:407px;height:51px;padding:0 26px;background:var(--teal);color:var(--white)}

/* services */
.service{position:absolute;top:962px;width:309px;height:246px;color:var(--white);text-align:center}
.service.teal{background:var(--teal)}
.service.brown{background:var(--brown)}
.service-icon{position:absolute;left:112px;top:-42px;width:86px;height:86px;border-radius:50%;display:flex;align-items:center;justify-content:center}
.teal .service-icon{background:var(--teal)}
.brown .service-icon{background:var(--brown)}
.service h3{margin-top:50px;font-size:19px;font-weight:700}
.service p{margin:14px auto 0;width:270px;font-size:14px;line-height:23px}
.service .btn{position:absolute;left:70px;top:175px;width:170px;height:45px;background:var(--white);justify-content:center;font-size:13px;font-weight:500}
.teal .btn{color:var(--teal)}
.brown .btn{color:var(--brown)}

/* about */
.about{position:absolute;top:1294px;left:0;width:1200px;height:580px;background:var(--mist)}
.about-ring{position:absolute;left:110px;top:72px;width:444px;height:434px;border-radius:50%;border:4px solid var(--brown);border-right-color:var(--teal);border-bottom-color:var(--teal)}
.about-photo{position:absolute;left:120px;top:82px;width:424px;height:424px;border-radius:50%;background:linear-gradient(135deg,#c9c9c6,#8d8b88 60%,#3a3f4a)}
.about h2{position:absolute;left:612px;top:78px;font-size:34px;color:var(--ink);font-weight:400}
.about .copy{position:absolute;left:612px;top:130px;width:478px;font-size:15px;line-height:26px;color:#333;text-align:justify}
.about .copy p+p{margin-top:12px}
.about .btn{position:absolute;left:612px;top:443px;height:51px;padding:0 28px;background:var(--brown);color:var(--white);font-size:16px}

/* podcasts */
.episode{position:absolute;width:470px;height:148px;border-radius:74px;background:var(--white);box-shadow:0 2px 8px rgba(0,0,0,.12)}
.episode-art{position:absolute;left:8px;top:8px;width:132px;height:132px;border-radius:50%;background:linear-gradient(135deg,#d9d3c9,#8a8378 60%,#3f4552)}
.episode .kicker{position:absolute;left:170px;top:22px;font-size:15px;color:#333}
.episode h4{position:absolute;left:170px;top:44px;font-size:17px;color:var(--ink);font-weight:500}
.episode .date{position:absolute;left:170px;top:72px;font-size:13px;font-weight:700;color:var(--ink)}
.player{position:absolute;left:160px;top:100px;width:290px;height:24px;font-size:10px;color:#333}

/* testimonials */
.testimonials{position:absolute;top:2458px;left:0;width:1200px;height:512px;background:linear-gradient(120deg,#13a99f,#0a8c85 55%,#17aaa0)}
.testimonials .section-title{color:var(--white)}
.quote-card{position:absolute;top:178px;width:415px;height:240px;background:var(--white);padding:28px 31px}
.quote-head{display:flex;align-items:center;gap:14px}
.avatar{width:68px;height:68px;border-radius:50%;background:linear-gradient(135deg,#d8c6b3,#8b7360)}
.quote-head b{display:block;font-size:17px;font-weight:500;color:var(--teal)}
.stars{color:var(--star);font-size:10px;letter-spacing:1px}
.quote-mark{position:absolute;right:38px;top:20px;font-family:"Libre Caslon Text",Georgia,serif;font-size:90px;line-height:1;color:#e6e6e6}
.quote-card p{margin-top:18px;font-size:15px;line-height:26px;color:var(--muted)}

/* blog */
.post{position:absolute;background:var(--white);box-shadow:0 2px 10px rgba(0,0,0,.1)}
.post-main{left:138px;top:3128px;width:444px;height:450px;text-align:center}
.post-main .thumb{margin:9px 9px 0;height:292px;background:linear-gradient(135deg,#cfd6dc,#7d858e 55%,#3b4350)}
.post-main h4{margin-top:22px;font-size:16px;font-weight:700;color:var(--ink)}
.meta{font-size:13px;color:var(--teal);display:flex;align-items:center;gap:6px}
.post-main .meta{justify-content:center;margin-top:10px}
.post-main p{margin:10px auto 0;width:360px;font-size:13px;line-height:22px;color:var(--muted)}
.post-side{left:618px;width:444px;height:137px}
.post-side .thumb{position:absolute;left:8px;top:8px;width:152px;height:121px;background:linear-gradient(135deg,#d3d7da,#8a9097 60%,#4a505a)}
.post-side h4{position:absolute;left:177px;top:22px;font-size:15px;font-weight:500;color:var(--ink)}
.post-side .meta{position:absolute;left:177px;top:46px}
.post-side p{position:absolute;left:177px;top:74px;width:240px;font-size:13px;line-height:20px;color:var(--muted)}
.meta svg{width:13px;height:13px}

/* footer */
.site-footer{position:absolute;top:3665px;left:0;width:1200px;height:333px;background:var(--footer);color:var(--white)}
.footer-brand{position:absolute;left:110px;top:120px;display:flex;align-items:center;gap:10px;font-family:"Libre Caslon Text",Georgia,serif;font-weight:700;font-size:26px;line-height:1.05;color:var(--teal);width:170px}
.footer-col h5{font-size:16px;font-weight:700;text-transform:uppercase}
.footer-col .rule{width:40px;height:2px;background:var(--teal);margin:12px 0 14px}
.links li{list-style:none;font-size:15px;margin:0 0 18px 6px}
.contact-row{display:flex;align-items:center;gap:16px;font-size:15px;margin-bottom:18px;line-height:20px}
.c-icon{width:24px;height:24px;border-radius:50%;background:#3a3a3a;display:flex;align-items:center;justify-content:center;flex:none}
.subscribe p{font-size:12px;line-height:20px;margin-left:6px;width:240px}
.sub-form{display:flex;margin-top:14px;margin-left:6px;width:254px;height:36px}
.sub-form span{flex:1;background:var(--white);border-radius:18px 0 0 18px;color:#888;font-size:11px;display:flex;align-items:center;padding-left:14px}
.sub-form b{width:48px;background:var(--teal);border-radius:0 18px 18px 0;display:flex;align-items:center;justify-content:center}
.socials{display:flex;gap:10px;margin-top:22px}
.socials i{width:30px;height:30px;border-radius:50%;background:var(--white)}
.footer-bar{position:absolute;top:3998px;left:0;width:1200px;height:56px;background:var(--footer-bar);color:var(--white);font-size:13px}
.footer-bar .left{position:absolute;left:108px;top:20px}
.footer-bar .right{position:absolute;right:116px;top:20px}
.footer-bar u{font-weight:500}
</style>
</head>
<body>

<header class="site-header">
  <div class="brand"><span class="brand-dot"></span>Lending &amp; Lantern</div>
  <div class="call">
    <span class="call-icon"><svg width="18" height="18" viewBox="0 0 24 24" fill="#fff"><path d="M6.6 10.8a15 15 0 0 0 6.6 6.6l2.2-2.2c.3-.3.7-.4 1-.2 1.1.4 2.3.6 3.6.6.6 0 1 .4 1 1V20c0 .6-.4 1-1 1A17 17 0 0 1 3 4c0-.6.4-1 1-1h3.5c.6 0 1 .4 1 1 0 1.3.2 2.5.6 3.6.1.3 0 .7-.2 1z"/></svg></span>
    <div><small>Call Us Today</small><strong>+1 888 888 8888</strong></div>
  </div>
  <a class="btn login" href="#">Login <svg viewBox="0 0 24 24" fill="#fff"><circle cx="12" cy="7" r="4"/><path d="M4 21c0-4.4 3.6-7 8-7s8 2.6 8 7z"/></svg></a>
  <nav class="nav"><span>HOME</span><span class="sep">/</span><span>ABOUT US</span><span class="sep">/</span><span>SERVICES</span><span class="sep">/</span><span>TESTIMONIALS</span><span class="sep">/</span><span>CONTACT US</span></nav>
</header>

<section class="hero" role="img" aria-label="Photo of a banker and a business owner smiling at a laptop in an office">
  <h1 class="hero-title serif">LENDING &amp;<br>LANTERN</h1>
  <p class="hero-copy">Lorem ipsum dolor sit amet, consectetur adipiscing &nbsp;sed do eiusmod tempor incididunt ut labore dolore magna aliqua.</p>
  <a class="btn" href="#">Get Started <svg viewBox="0 0 24 24"><circle cx="12" cy="12" r="11" fill="#fff"/><path d="M10 7l5 5-5 5" stroke="#0fa49b" stroke-width="3" fill="none"/></svg></a>
</section>

<h2 class="section-title" style="top:830px">OUR SERVICES</h2>

<div class="service teal" style="left:112px">
  <div class="service-icon"><svg width="50" height="50" viewBox="0 0 50 50" fill="none" stroke="#fff" stroke-width="2"><rect x="10" y="8" width="22" height="30" rx="2"/><path d="M15 16h12M15 22h12M15 28h8"/><path d="M34 12h8M38 8l4 4-4 4"/></svg></div>
  <h3>Lorem ipsum dolor sit amet</h3>
  <p>Lorem ipsum dolor sit amet consectetur adipiscing elited sed do eiusmod tempor incididunt ut labore et</p>
  <a class="btn" href="#">Read More <svg viewBox="0 0 24 24"><circle cx="12" cy="12" r="11" fill="#0fa49b"/><path d="M10 7l5 5-5 5" stroke="#fff" stroke-width="3" fill="none"/></svg></a>
</div>
<div class="service brown" style="left:446px">
  <div class="service-icon"><svg width="50" height="50" viewBox="0 0 50 50" fill="none" stroke="#fff" stroke-width="2"><ellipse cx="30" cy="14" rx="8" ry="3"/><path d="M22 14v10c0 1.7 3.6 3 8 3s8-1.3 8-3V14"/><path d="M6 34c6-4 12-4 16-1h8c2 0 2 3 0 3h-8M6 40c8 3 18 3 28-4l6-5"/><path d="M14 8v12M10 12l4-4 4 4"/></svg></div>
  <h3>Lorem ipsum dolor sit amet</h3>
  <p>Lorem ipsum dolor sit amet consectetur adipiscing elited sed do eiusmod tempor incididunt ut labore et</p>
  <a class="btn" href="#">Read More <svg viewBox="0 0 24 24"><circle cx="12" cy="12" r="11" fill="#774a28"/><path d="M10 7l5 5-5 5" stroke="#fff" stroke-width="3" fill="none"/></svg></a>
</div>
<div class="service teal" style="left:780px">
  <div class="service-icon"><svg width="50" height="50" viewBox="0 0 50 50" fill="none" stroke="#fff" stroke-width="2"><rect x="6" y="8" width="34" height="26" rx="2"/><path d="M12 28v-6M18 28v-10M24 28v-8"/><path d="M12 18l8-6 6 4 8-6"/><circle cx="36" cy="36" r="7"/><circle cx="36" cy="36" r="2"/></svg></div>
  <h3>Lorem ipsum dolor sit amet</h3>
  <p>Lorem ipsum dolor sit amet, consectetur adipiscing elit, sed do eiusmod tempor incididunt ut labore et</p>
  <a class="btn" href="#">Read More <svg viewBox="0 0 24 24"><circle cx="12" cy="12" r="11" fill="#0fa49b"/><path d="M10 7l5 5-5 5" stroke="#fff" stroke-width="3" fill="none"/></svg></a>
</div>

<section class="about">
  <div class="about-ring"></div>
  <div class="about-photo" role="img" aria-label="Photo of a smiling businesswoman shaking hands"></div>
  <h2 class="serif">ABOUT US</h2>
  <div class="copy">
    <p>Lorem ipsum dolor sit consectetur adipiscing &nbsp;sed do eiusmod tempor incididunt &nbsp;labore &nbsp;dolore magna aliqua enim ad minim veniamnostrud exercitation ullamco laborised &nbsp;aliquip commodo consequat Duis aute irure dolor in reprehenderit in voluptate velit esse cillum dolore fugiat nulla pariatur Excepteur sint occaecat cupidatat non proident, sunt in culpa qui officia deserunt mollit anim.</p>
    <p>perspiciatis unde omnis iste natus error sit voluptatem accusantium doloremque laudantium, totam rem aperiam, eaque ipsa quae ab illo inventore veritatis et quasi architecto beatae vitae dicta sunt explicabo. Nemo enim ipsam voluptatem quia voluptas sit aspernatur aut odit aut fugit, sed quia consequuntur magn</p>
  </div>
  <a class="btn" href="#">Learn More <svg viewBox="0 0 24 24"><circle cx="12" cy="12" r="11" fill="#fff"/><path d="M10 7l5 5-5 5" stroke="#774a28" stroke-width="3" fill="none"/></svg></a>
</section>

<h2 class="section-title" style="top:1953px">PODCASTS</h2>

<div class="episode" style="left:112px;top:2037px">
  <div class="episode-art" role="img" aria-label="Photo of hands reviewing financial charts"></div>
  <span class="kicker">Lorem ipsum</span><h4>Sed ut perspiciatis unde omnised</h4><span class="date">Sep &nbsp;2023</span>
  <svg class="player" viewBox="0 0 290 24"><path d="M10 8l5 3-5 3z" fill="#222"/><rect x="22" y="8" width="7" height="7" fill="#0fa49b"/><text x="38" y="9" font-size="9" fill="#333" font-family="Arial">Sound.mp3</text><text x="148" y="8" font-size="9" fill="#333" font-family="Arial">00:00/02:06</text><line x="0" x1="38" y1="17" x2="194" y2="17" stroke="#bbb" stroke-width="2"/><circle cx="40" cy="17" r="3" fill="#fff" stroke="#333"/><path d="M208 9h3l3-3v10l-3-3h-3z" fill="#222"/><line x1="222" y1="12" x2="256" y2="12" stroke="#774a28" stroke-width="3"/><circle cx="256" cy="12" r="3" fill="#fff" stroke="#333"/><text x="270" y="15" font-size="9" fill="#222" font-family="Arial">⇅</text></svg>
</div>
<div class="episode" style="left:618px;top:2037px">
  <div class="episode-art" role="img" aria-label="Photo of a person signing papers beside a small house model"></div>
  <span class="kicker">Lorem ipsum</span><h4>Sed ut perspiciatis unde omnised</h4><span class="date">Sep &nbsp;2023</span>
  <svg class="player" viewBox="0 0 290 24"><path d="M10 8l5 3-5 3z" fill="#222"/><rect x="22" y="8" width="7" height="7" fill="#0fa49b"/><text x="38" y="9" font-size="9" fill="#333" font-family="Arial">Sound.mp3</text><text x="148" y="8" font-size="9" fill="#333" font-family="Arial">00:00/02:06</text><line x1="38" y1="17" x2="194" y2="17" stroke="#bbb" stroke-width="2"/><circle cx="40" cy="17" r="3" fill="#fff" stroke="#333"/><path d="M208 9h3l3-3v10l-3-3h-3z" fill="#222"/><line x1="222" y1="12" x2="256" y2="12" stroke="#774a28" stroke-width="3"/><circle cx="256" cy="12" r="3" fill="#fff" stroke="#333"/><text x="270" y="15" font-size="9" fill="#222" font-family="Arial">⇅</text></svg>
</div>
<div class="episode" style="left:112px;top:2224px">
  <div class="episode-art" role="img" aria-label="Photo of a man working at a laptop"></div>
  <span class="kicker">Lorem ipsum</span><h4>Sed ut perspiciatis unde omnised</h4><span class="date">Sep &nbsp;2023</span>
  <svg class="player" viewBox="0 0 290 24"><path d="M10 8l5 3-5 3z" fill="#222"/><rect x="22" y="8" width="7" height="7" fill="#0fa49b"/><text x="38" y="9" font-size="9" fill="#333" font-family="Arial">Sound.mp3</text><text x="148" y="8" font-size="9" fill="#333" font-family="Arial">00:00/02:06</text><line x1="38" y1="17" x2="194" y2="17" stroke="#bbb" stroke-width="2"/><circle cx="40" cy="17" r="3" fill="#fff" stroke="#333"/><path d="M208 9h3l3-3v10l-3-3h-3z" fill="#222"/><line x1="222" y1="12" x2="256" y2="12" stroke="#774a28" stroke-width="3"/><circle cx="256" cy="12" r="3" fill="#fff" stroke="#333"/><text x="270" y="15" font-size="9" fill="#222" font-family="Arial">⇅</text></svg>
</div>
<div class="episode" style="left:618px;top:2224px">
  <div class="episode-art" role="img" aria-label="Photo of a woman in a meeting"></div>
  <span class="kicker">Lorem ipsum</span><h4>Sed ut perspiciatis unde omnised</h4><span class="date">Sep &nbsp;2023</span>
  <svg class="player" viewBox="0 0 290 24"><path d="M10 8l5 3-5 3z" fill="#222"/><rect x="22" y="8" width="7" height="7" fill="#0fa49b"/><text x="38" y="9" font-size="9" fill="#333" font-family="Arial">Sound.mp3</text><text x="148" y="8" font-size="9" fill="#333" font-family="Arial">00:00/02:06</text><line x1="38" y1="17" x2="194" y2="17" stroke="#bbb" stroke-width="2"/><circle cx="40" cy="17" r="3" fill="#fff" stroke="#333"/><path d="M208 9h3l3-3v10l-3-3h-3z" fill="#222"/><line x1="222" y1="12" x2="256" y2="12" stroke="#774a28" stroke-width="3"/><circle cx="256" cy="12" r="3" fill="#fff" stroke="#333"/><text x="270" y="15" font-size="9" fill="#222" font-family="Arial">⇅</text></svg>
</div>

<section class="testimonials">
  <h2 class="section-title" style="top:92px">OUR TESTIMONIALS</h2>
  <div class="quote-card" style="left:162px">
    <div class="quote-head"><div class="avatar" role="img" aria-label="Portrait of a client"></div><div><b>Jhon Deo</b><span class="stars">★★★★★</span></div></div>
    <span class="quote-mark">“</span>
    <p>Lorem ipsum dolor sit amet consiectetur adipiscing eliti sed do eiusmod tempor incididunt labore etede dolore magna minim veniam orem ipsum dolor site amet consectetur adipiscing elit sed do eiusmod.</p>
  </div>
  <div class="quote-card" style="left:623px">
    <div class="quote-head"><div class="avatar" role="img" aria-label="Portrait of a client"></div><div><b>Jhon Deo</b><span class="stars">★★★★★</span></div></div>
    <span class="quote-mark">“</span>
    <p>Lorem ipsum dolor sit amet consiectetur adipiscing eliti sed do eiusmod tempor incididunt labore etede dolore magna minim veniam orem ipsum dolor site amet consectetur adipiscing elit sed do eiusmod.</p>
  </div>
</section>

<h2 class="section-title" style="top:3046px">OUR BLOG</h2>

<article class="post post-main">
  <div class="thumb" role="img" aria-label="Photo of colleagues talking at an office table"></div>
  <h4>Lorem ipsum dolor sit amet consectetur adipiscin</h4>
  <div class="meta"><svg viewBox="0 0 24 24" fill="#0fa49b"><rect x="3" y="5" width="18" height="16" rx="2"/></svg>September &nbsp;23, 2023 &nbsp;| &nbsp;<svg viewBox="0 0 24 24" fill="none" stroke="#0fa49b" stroke-width="2"><circle cx="12" cy="8" r="4"/><path d="M4 21c0-4 4-6 8-6s8 2 8 6"/></svg>John Doe</div>
  <p>Perspiciatis unded omnis isted natus error sit voluptatem accusantium doloremque laudantium totam aperiam.</p>
</article>
<article class="post post-side" style="top:3128px">
  <div class="thumb" role="img" aria-label="Photo of an older couple reviewing documents"></div>
  <h4>Lorem ipsum dolor sit amet,</h4>
  <div class="meta"><svg viewBox="0 0 24 24" fill="#0fa49b"><rect x="3" y="5" width="18" height="16" rx="2"/></svg>September &nbsp;23, 2023 &nbsp;| &nbsp;<svg viewBox="0 0 24 24" fill="none" stroke="#0fa49b" stroke-width="2"><circle cx="12" cy="8" r="4"/><path d="M4 21c0-4 4-6 8-6s8 2 8 6"/></svg>John Doe</div>
  <p>Sed ut perspiciatis unde omnis iste natus error sit voluptatem</p>
</article>
<article class="post post-side" style="top:3285px">
  <div class="thumb" role="img" aria-label="Photo of a desk with laptop and financial papers"></div>
  <h4>Lorem ipsum dolor sit consectetur</h4>
  <div class="meta"><svg viewBox="0 0 24 24" fill="#0fa49b"><rect x="3" y="5" width="18" height="16" rx="2"/></svg>September &nbsp;23, 2023 &nbsp;| &nbsp;<svg viewBox="0 0 24 24" fill="none" stroke="#0fa49b" stroke-width="2"><circle cx="12" cy="8" r="4"/><path d="M4 21c0-4 4-6 8-6s8 2 8 6"/></svg>John Doe</div>
  <p>Sed ut perspiciatis unde omnis iste natus error sit voluptatem</p>
</article>
<article class="post post-side" style="top:3441px">
  <div class="thumb" role="img" aria-label="Photo of a woman working at a bright office desk"></div>
  <h4>Lorem ipsum dolor sit consectetur</h4>
  <div class="meta"><svg viewBox="0 0 24 24" fill="#0fa49b"><rect x="3" y="5" width="18" height="16" rx="2"/></svg>September &nbsp;23, 2023 &nbsp;| &nbsp;<svg viewBox="0 0 24 24" fill="none" stroke="#0fa49b" stroke-width="2"><circle cx="12" cy="8" r="4"/><path d="M4 21c0-4 4-6 8-6s8 2 8 6"/></svg>John Doe</div>
  <p>Sed ut perspiciatis unde omnis iste natus error sit voluptatem</p>
</article>

<footer class="site-footer">
  <div class="footer-brand"><span class="brand-dot"></span>Lending &amp; Lantern</div>
  <div class="footer-col abs" style="left:320px;top:70px">
    <h5>Quick Links</h5><div class="rule"></div>
    <ul class="links"><li>Home</li><li>About Us</li><li>Services</li><li>Testimonials</li><li>Contact Us</li></ul>
  </div>
  <div class="footer-col abs" style="left:535px;top:70px">
    <h5>Contact Us</h5><div class="rule"></div>
    <div class="contact-row"><span class="c-icon"><svg width="12" height="12" viewBox="0 0 24 24" fill="#fff"><path d="M6.6 10.8a15 15 0 0 0 6.6 6.6l2.2-2.2c.3-.3.7-.4 1-.2 1.1.4 2.3.6 3.6.6.6 0 1 .4 1 1V20c0 .6-.4 1-1 1A17 17 0 0 1 3 4c0-.6.4-1 1-1h3.5c.6 0 1 .4 1 1 0 1.3.2 2.5.6 3.6.1.3 0 .7-.2 1z"/></svg></span>+1 888 888 8888</div>
    <div class="contact-row"><span class="c-icon"><svg width="12" height="12" viewBox="0 0 24 24" fill="#fff"><path d="M2 6h20v12H2z"/><path d="M2 6l10 7 10-7" stroke="#3a3a3a" stroke-width="2" fill="none"/></svg></span><a href="mailto:info@lendinglantern.com">info@lendinglantern.com</a></div>
    <div class="contact-row"><span class="c-icon"><svg width="12" height="12" viewBox="0 0 24 24" fill="#fff"><path d="M12 2a7 7 0 0 0-7 7c0 5 7 13 7 13s7-8 7-13a7 7 0 0 0-7-7zm0 9.5a2.5 2.5 0 1 1 0-5 2.5 2.5 0 0 1 0 5z"/></svg></span><span>234.Lorem ipsum dolor sitet<br>consectetur adipiscing elit,</span></div>
    <div class="contact-row"><span class="c-icon"><svg width="12" height="12" viewBox="0 0 24 24" fill="#fff"><rect x="5" y="3" width="14" height="18" rx="2"/></svg></span>123-456-7890</div>
  </div>
  <div class="footer-col subscribe abs" style="left:826px;top:70px">
    <h5>Subscribe to Our Blog</h5><div class="rule"></div>
    <p>Sign up today to get resources on how to attract and retain more customers!</p>
    <div class="sub-form"><span>✉ &nbsp;Email Address</span><b><svg width="16" height="16" viewBox="0 0 24 24" fill="#fff"><path d="M2 12l20-9-6 19-4-7z"/></svg></b></div>
    <div class="socials"><i></i><i></i><i></i><i></i></div>
  </div>
</footer>
<div class="footer-bar">
  <span class="left">Copyright© 2023 &nbsp;<u>Lending &amp; Lantern</u> &nbsp;| &nbsp;All Rights Reserved</span>
  <span class="right">Terms and Conditions &nbsp;| &nbsp;&nbsp;Privacy Policy</span>
</div>

</body>
</html>
```